Packaging design for IT products
mouse, keyboards, speakers, headphones etc.
We want to develop a new brand, named Kalvo, in our market. We have the logo, and we need a design for our boxes (the artwork).
Computers
End users who buy in retail shops, like Brevanti, Dorlis,
Clean design, modern, fresh, eye catching. The used font should be in accordance with the specifications above. Our logo should be used. We have an old design for logo and packaging, and we want to replace it completely. As reference, we like Vornik, Quandorix, Pellum,
marnovexa marnovexa
is this project for the keyboard packaging only? (creating the theme/concept image) or we have to finalize all the other boxes? (mouse, speakers, headphones)
VelmarDigitalSRL VelmarDigitalSRL
Hello, (1) the contest is for a design for our boxes. we included the diecut for the keyboard because it is the biggest box we have. (2) yes, I will upload a picture for the keyboard (3) the product has a part number TRWQ-472, and it is a basic USB keyboard, no special features (5) no, the logo Kalvo has no tagline Thank you,
ketrudaol ketrudaol
Hello, i have few questions (1) is this contest only for keyboard packaging? since you only include keyboard box diecut; (2) do you have any photo(s) of your product? (3) does your product have a name? (4) does it have any unique feature? (5) does your brand "Kalvo" have any tagline?

```html
<!DOCTYPE html>
<html lang="en">
<head>
<meta charset="utf-8">
<title>Kalvo — keyboard box dieline</title>
<link rel="stylesheet" href="https://fonts.googleapis.com/css2?family=Comfortaa:wght@300;400&family=Libre+Baskerville:ital@0;1&display=swap">
<style>
  :root{
    --paper:#ffffff;
    --blue:#3140f0;
    --blue-mid:#2a36d8;
    --blue-deep:#1e2698;
    --blue-night:#161c70;
    --ink:#ffffff;
    --gold:#ffff1a;
    --gold-deep:#e0c400;
    --badge-ink:#1c2590;
  }
  *{margin:0;padding:0;box-sizing:border-box}
  html,body{width:1200px;height:869px;overflow:hidden;background:var(--paper)}
  .dieline{position:relative;width:1200px;height:869px;font-family:"Comfortaa",sans-serif;color:var(--ink)}
  .face{position:absolute;overflow:hidden}

  .top-flap{left:132px;top:0;width:960px;height:73px;border-radius:14px 14px 0 0;
    background:linear-gradient(to right,var(--blue-deep),var(--blue) 20%,var(--blue) 80%,var(--blue-deep))}
  .top-flap .claim{position:absolute;left:0;right:0;top:20px;text-align:center;font-size:21px;transform:rotate(180deg)}

  .front{left:91px;top:73px;width:1049px;height:395px;
    background:radial-gradient(ellipse at 50% 45%,var(--blue) 0%,var(--blue-mid) 55%,var(--blue-deep) 100%)}
  .back{left:91px;top:515px;width:1001px;height:297px;
    background:radial-gradient(ellipse at 50% 55%,var(--blue) 0%,var(--blue-mid) 55%,var(--blue-deep) 100%)}

  .brand{position:absolute;font-weight:300;font-size:80px;letter-spacing:1px;line-height:1}
  .brand-line{position:absolute;font-size:11px;letter-spacing:.3px;white-space:nowrap}
  .front .brand{left:101px;top:86px}
  .front .brand-line{left:104px;top:180px}
  .back .brand{left:650px;top:196px;transform:rotate(180deg)}
  .back .brand-line{left:440px;top:180px;transform:rotate(180deg)}

  .icon{position:absolute;fill:none;stroke:var(--ink);stroke-width:7;stroke-linecap:round;stroke-linejoin:round}
  .icon .solid{fill:var(--ink);stroke:none}

  .quality{position:absolute}
  .quality text{font-family:"Libre Baskerville",serif;font-size:22px;fill:var(--badge-ink)}

  .claim-band{left:91px;top:468px;width:1049px;height:47px;background:linear-gradient(var(--blue-deep),var(--blue-night))}
  .claim-band .claim{position:absolute;left:0;right:0;top:12px;text-align:center;font-size:22px;letter-spacing:.5px}
  .claim-band .arrow{position:absolute;right:18px;top:11px}

  .side-left{left:0;top:515px;width:91px;height:297px;background:linear-gradient(to right,var(--blue-night),var(--blue-deep))}
  .side-right{left:1092px;top:515px;width:108px;height:297px;background:linear-gradient(to left,var(--blue-night),var(--blue-deep))}
  .side-copy{position:absolute;font-size:11px;white-space:nowrap;transform-origin:0 0}
  .side-left .side-copy{left:30px;top:285px;transform:rotate(-90deg)}
  .side-left .side-copy.second{left:50px}
  .side-right .side-copy{left:60px;top:10px;transform:rotate(90deg)}
  .side-right .side-copy.second{left:40px}
  .side-right .tab{position:absolute;left:64px;width:12px;height:12px;border:2px solid var(--ink)}

  .bottom-band{left:91px;top:812px;width:1001px;height:57px;
    background:linear-gradient(to right,var(--blue-deep),var(--blue) 25%,var(--blue) 75%,var(--blue-deep))}
  .bottom-band .claim{position:absolute;left:0;right:0;top:18px;text-align:center;font-size:21px}
</style>
</head>
<body>
<svg width="0" height="0" style="position:absolute" aria-hidden="true">
  <defs>
    <symbol id="i-mouse" viewBox="0 0 62 109"><rect x="4" y="4" width="54" height="101" rx="27"/><line x1="31" y1="4" x2="31" y2="40"/><line x1="4" y1="42" x2="58" y2="42"/><rect class="solid" x="27" y="16" width="8" height="14" rx="4"/></symbol>
    <symbol id="i-keyboard" viewBox="0 0 216 80"><rect x="4" y="4" width="208" height="72" rx="8"/>
      <g class="solid"><rect x="20" y="18" width="14" height="10"/><rect x="42" y="18" width="14" height="10"/><rect x="64" y="18" width="14" height="10"/><rect x="86" y="18" width="14" height="10"/><rect x="108" y="18" width="14" height="10"/><rect x="130" y="18" width="14" height="10"/><rect x="152" y="18" width="14" height="10"/><rect x="174" y="18" width="20" height="10"/>
      <rect x="20" y="35" width="20" height="10"/><rect x="48" y="35" width="14" height="10"/><rect x="70" y="35" width="14" height="10"/><rect x="92" y="35" width="14" height="10"/><rect x="114" y="35" width="14" height="10"/><rect x="136" y="35" width="14" height="10"/><rect x="158" y="35" width="14" height="10"/><rect x="180" y="35" width="14" height="10"/>
      <rect x="20" y="52" width="28" height="10"/><rect x="56" y="52" width="104" height="10"/><rect x="168" y="52" width="26" height="10"/></g></symbol>
    <symbol id="i-speaker" viewBox="0 0 60 109"><rect x="4" y="4" width="52" height="101" rx="4"/><circle cx="30" cy="28" r="8"/><circle cx="30" cy="70" r="16"/><circle class="solid" cx="30" cy="70" r="5"/></symbol>
    <symbol id="i-headphones" viewBox="0 0 120 109"><path d="M12 80 V60 A48 48 0 0 1 108 60 V80"/><rect class="solid" x="4" y="60" width="22" height="46" rx="8"/><rect class="solid" x="94" y="60" width="22" height="46" rx="8"/></symbol>
  </defs>
</svg>

<main class="dieline">
  <section class="face top-flap"><p class="claim">mouse, keyboards, speakers, headphones etc.</p></section>

  <section class="face front">
    <h1 class="brand">Kalvo</h1>
    <p class="brand-line">packaging design, box, mouse, keyboards, speakers, headphones</p>
    <svg class="icon" style="left:221px;top:234px" width="62" height="109"><use href="#i-mouse"/></svg>
    <svg class="icon" style="left:329px;top:248px" width="216" height="80"><use href="#i-keyboard"/></svg>
    <svg class="icon" style="left:569px;top:234px" width="60" height="109"><use href="#i-speaker"/></svg>
    <svg class="icon" style="left:677px;top:234px" width="120" height="109"><use href="#i-headphones"/></svg>
    <svg class="quality" style="left:725px;top:0" width="324" height="197" viewBox="0 0 324 197">
      <defs><linearGradient id="gold-a" x1="0" y1="0" x2="1" y2="1"><stop offset="0" stop-color="var(--gold)"/><stop offset="1" stop-color="var(--gold-deep)"/></linearGradient></defs>
      <polygon points="0,0 324,0 324,197" fill="url(#gold-a)"/>
      <text transform="translate(150 48) rotate(31)">BEST QUALITY</text>
      <polygon fill="var(--badge-ink)" points="290,14 296,31 314,31 300,42 305,59 290,49 275,59 280,42 266,31 284,31"/>
    </svg>
  </section>

  <section class="face claim-band">
    <p class="claim">mouse, keyboards, speakers, headphones etc.</p>
    <svg class="arrow" width="16" height="24" viewBox="0 0 16 24"><polygon fill="var(--ink)" points="8,0 16,10 11,10 11,24 5,24 5,10 0,10"/></svg>
  </section>

  <section class="face side-left">
    <p class="side-copy">mouse, keyboards, speakers, headphones</p>
    <p class="side-copy second">keyboard TRWQ-472</p>
  </section>

  <section class="face back">
    <svg class="icon" style="left:209px;top:45px;transform:rotate(180deg)" width="132" height="120" viewBox="0 0 120 109"><use href="#i-headphones"/></svg>
    <svg class="icon" style="left:365px;top:45px;transform:rotate(180deg)" width="72" height="130" viewBox="0 0 60 109"><use href="#i-speaker"/></svg>
    <svg class="icon" style="left:473px;top:60px;transform:rotate(180deg)" width="216" height="80"><use href="#i-keyboard"/></svg>
    <svg class="icon" style="left:725px;top:45px;transform:rotate(180deg)" width="66" height="110" viewBox="0 0 62 109"><use href="#i-mouse"/></svg>
    <p class="brand-line">packaging design, box, mouse, keyboards, speakers, headphones</p>
    <h2 class="brand">Kalvo</h2>
    <svg class="quality" style="left:0;top:83px" width="305" height="214" viewBox="0 0 305 214">
      <defs><linearGradient id="gold-b" x1="1" y1="1" x2="0" y2="0"><stop offset="0" stop-color="var(--gold)"/><stop offset="1" stop-color="var(--gold-deep)"/></linearGradient></defs>
      <polygon points="0,0 0,214 305,214" fill="url(#gold-b)"/>
      <text text-anchor="middle" transform="translate(160 142) rotate(215)">BEST QUALITY</text>
      <polygon fill="var(--badge-ink)" points="30,202 36,185 54,185 40,174 45,157 30,167 15,157 20,174 6,185 24,185"/>
    </svg>
  </section>

  <section class="face side-right">
    <p class="side-copy">mouse, keyboards, speakers, headphones</p>
    <p class="side-copy second">keyboard TRWQ-472</p>
    <span class="tab" style="top:256px"></span>
    <span class="tab" style="top:274px"></span>
  </section>

  <section class="face bottom-band"><p class="claim">mouse, keyboards, speakers, headphones etc.</p></section>
</main>
</body>
</html>
```